Brookvale Services telephone book advert

Design a tellwick directory telephone book advertisement. Attached is a current version of the brookvale services advert. Please use the same information as detailed on the existing advert but arty!. Overall size should be 130 mm by 91 mm portrait using one of the specified colours plus black. Any background should be opaque (not white). and delivered in the formats as specified.

```html
<!DOCTYPE html>
<html lang="en">
<head>
<meta charset="utf-8">
<title>Brookvale Services – Directory Advert</title>
<link rel="stylesheet" href="https://fonts.googleapis.com/css2?family=Montserrat:wght@700;800&family=Roboto+Condensed:wght@300;400;700&display=swap">
<style>
  :root {
    --brand-blue: #005eb0;
    --cream: #fffacd;
    --title-cream: #fff8c8;
    --panel-grey: #bcbdc0;
    --ink: #000000;
    --white: #ffffff;
  }
  * { margin: 0; padding: 0; box-sizing: border-box; }
  html, body { width: 840px; height: 1200px; overflow: hidden; background: var(--brand-blue); }
  .advert {
    position: relative; width: 840px; height: 1200px;
    background: var(--brand-blue);
    font-family: "Roboto Condensed", "Arial Narrow", sans-serif;
  }
  .brand-title { position: absolute; left: 0; top: 0; width: 840px; height: 291px; }
  .brand-title text { font-family: "Montserrat", sans-serif; fill: var(--title-cream); }
  .info-panel {
    position: absolute; left: 9px; top: 291px; width: 822px; height: 681px;
    background: var(--cream);
  }
  .tagline {
    position: absolute; left: 0; width: 840px; top: 310px; text-align: center;
    font-weight: 700; font-size: 43px; color: var(--ink); transform: scaleX(0.92);
  }
  .phone-line {
    position: absolute; left: 0; width: 840px; top: 360px; text-align: center;
    color: var(--ink); white-space: nowrap;
  }
  .phone-line .call { font-weight: 700; font-size: 52px; margin-right: 14px; }
  .phone-line .number {
    font-family: "Montserrat", sans-serif; font-weight: 800; font-size: 124px;
    letter-spacing: -2px; line-height: 1;
  }
  .service {
    position: absolute; width: 359px; height: 172px;
  }
  .service-head {
    height: 67px; background: var(--brand-blue); border-radius: 22px 22px 0 0;
    color: var(--title-cream); font-weight: 700; font-size: 40px;
    text-align: center; line-height: 67px;
  }
  .service-body {
    height: 105px; background: var(--panel-grey); color: var(--ink);
    font-weight: 700; font-size: 33px; line-height: 38px; text-align: center;
    padding-top: 13px;
  }
  .service.emergencies { left: 60px; top: 508px; }
  .service.maintenance { left: 437px; top: 508px; }
  .service.survey { left: 60px; top: 696px; }
  .service.rehabilitation { left: 437px; top: 696px; }
  .web-tab {
    position: absolute; left: 107px; top: 900px; width: 618px; height: 160px;
    background: var(--brand-blue); border-radius: 24px 24px 0 0;
  }
  .web-box {
    position: absolute; left: 121px; top: 912px; width: 591px; height: 134px;
    background: var(--panel-grey); border: 2px solid var(--white); border-radius: 22px;
    text-align: center; color: var(--ink);
  }
  .web-box .prompt { font-weight: 300; font-size: 29px; margin-top: 16px; line-height: 34px; }
  .web-box .url { font-weight: 700; font-size: 60px; line-height: 66px; }
  .contact-manager {
    position: absolute; left: 0; width: 840px; top: 1058px; text-align: center;
    color: var(--title-cream); white-space: nowrap;
  }
  .contact-manager .role { font-weight: 300; font-size: 38px; }
  .contact-manager .name { font-weight: 700; font-size: 54px; }
  .address {
    position: absolute; left: 0; width: 840px; top: 1145px; text-align: center;
    color: var(--title-cream); font-weight: 700; font-size: 36px; white-space: nowrap;
  }
</style>
</head>
<body>
<div class="advert">
  <svg class="brand-title" viewBox="0 0 840 291" aria-label="Brookvale Services Limited">
    <text x="90" y="153" font-size="122" font-weight="800" textLength="662" lengthAdjust="spacingAndGlyphs">BROOKVALE</text>
    <text x="88" y="246" font-size="90" font-weight="800" textLength="496" lengthAdjust="spacingAndGlyphs">SERVICES</text>
    <text x="606" y="215" font-size="38" font-weight="700" textLength="147" lengthAdjust="spacingAndGlyphs">LIMITED</text>
  </svg>

  <div class="info-panel"></div>
  <p class="tagline">For Local Drainage Expertise</p>
  <p class="phone-line"><span class="call">CALL</span><span class="number">318-642</span></p>

  <section class="service emergencies">
    <h2 class="service-head">EMERGENCIES</h2>
    <p class="service-body">Unblocking &amp;<br>High Pressure Cleaning</p>
  </section>
  <section class="service maintenance">
    <h2 class="service-head">MAINTENACE</h2>
    <p class="service-body">Jetting, De-Scaling<br>&amp; Root Cutting</p>
  </section>
  <section class="service survey">
    <h2 class="service-head">SURVEY</h2>
    <p class="service-body">Modern CCTV,<br>Condition Reports</p>
  </section>
  <section class="service rehabilitation">
    <h2 class="service-head">REHABILITATION</h2>
    <p class="service-body">Structural Re-lining of<br>Damaged &amp; Leaky Drains</p>
  </section>

  <div class="web-tab"></div>
  <div class="web-box">
    <p class="prompt">For more information please visit our website :</p>
    <p class="url">www.bvs.gg</p>
  </div>

  <p class="contact-manager"><span class="role">Contracts Manager : </span><span class="name">Owen Tallard</span></p>
  <p class="address">Mill Lane Crossing, Vale Harbour, Guernsey GY3 7PQ</p>
</div>
</body>
</html>
```